Ecard for facebook and Instagram postings

I need 4 ecards (don't know if that is what it is called) for Facebook and Instagram postings. My Logo and company name should be incorporated and also be square. I would like to be able to insert text as I need. Examples are:

https://www.pinwheelsocial.example/photo.php?fbid=20284619375028461&set=a.20273946105827394.718352.94735186024&type=1&relevant_count=1

https://media-b-ord.xx.tilecdnhub.example/pics-lke7/8765432_135792468013579_864209753_n.jpg

I don't necessarily need images on them, just the color scheme to my business cards and the logo and business name. But if you'd like to give it an interesting look, you can go ahead and play with it. My site is sunmeadowcoaching.example, if you'd like to see the style of it.

Thank you!!!
Updates

I just uploaded the logo in two variations.  Thank you!

Target Market(s)

Women 16-65

Industry/Entity Type

Business

Requirements
Must have
• Logo and business name
Should not have
• No white background. I have attached business card picture so you can have an idea of what I'd like.

```html
<!DOCTYPE html>
<html lang="en">
<head>
<meta charset="utf-8">
<title>Sun Meadow Coaching Services – Social Cards</title>
<link rel="stylesheet" href="https://fonts.googleapis.com/css2?family=Montserrat:wght@500;600&display=swap">
<style>
  :root {
    --canvas: #ffffff;
    --orange-soft: #f9ad58;
    --orange: #f6941f;
    --orange-line: #f08a1c;
    --glow: #fffaf2;
    --brand-red: #c1272d;
    --ink-grey: #555555;
    --white: #ffffff;
    --feature-light: rgba(255, 246, 232, 0.55);
    --feature-warm: rgba(214, 108, 52, 0.42);
    --feature-airy: rgba(238, 140, 70, 0.38);
  }
  html, body {
    margin: 0;
    padding: 0;
    width: 1200px;
    height: 1000px;
    overflow: hidden;
    background: var(--canvas);
  }
  .canvas {
    position: relative;
    width: 1200px;
    height: 1000px;
    font-family: "Montserrat", Arial, sans-serif;
  }
  .card {
    position: absolute;
    width: 360px;
    height: 360px;
    overflow: hidden;
  }
  .card--top-left     { left: 121px; top: 70px; }
  .card--top-right    { left: 720px; top: 70px; }
  .card--bottom-left  { left: 121px; top: 570px; }
  .card--bottom-right { left: 720px; top: 570px; }

  .card__glow {
    position: absolute;
    inset: 0;
  }
  .card--soft .card__glow {
    background: radial-gradient(circle at 179px 180px, var(--glow) 0%, #fde1bd 28%, var(--orange-soft) 62%, var(--orange-soft) 100%);
  }
  .card--vivid .card__glow {
    background: radial-gradient(circle at 179px 180px, var(--glow) 0%, #fddab0 26%, #f9b060 55%, var(--orange) 75%, var(--orange) 100%);
  }
  .card--airy .card__glow {
    background: radial-gradient(circle 182px at 179px 180px, #f9a850 0%, #fbc68a 40%, #fde4c6 72%, rgba(255,255,255,0) 100%);
  }
  .card--warm .card__glow {
    background: radial-gradient(circle at 179px 180px, var(--glow) 0%, #fcd3a6 26%, #f9ae5b 52%, var(--orange) 72%, var(--orange) 100%);
  }

  /* Large faint brand feature */
  .feature {
    position: absolute;
    left: 0;
    right: 0;
    top: 0;
    height: 334px;
  }
  .feature__ring {
    position: absolute;
    left: 62px;
    top: 28px;
    width: 236px;
    height: 236px;
    border-radius: 50%;
    border: 26px solid;
    box-sizing: border-box;
  }
  .feature__name {
    position: absolute;
    left: 0;
    right: 0;
    top: 104px;
    margin: 0;
    text-align: center;
    font-size: 58px;
    font-weight: 600;
    line-height: 0.98;
    letter-spacing: -1px;
  }
  .card--soft .feature__ring,
  .card--vivid .feature__ring { border-color: var(--feature-light); }
  .card--soft .feature__name,
  .card--vivid .feature__name { color: var(--feature-light); }
  .card--airy .feature__ring { border-color: var(--feature-airy); }
  .card--airy .feature__name { color: var(--feature-airy); }
  .card--warm .feature__ring { border-color: var(--feature-warm); }
  .card--warm .feature__name { color: var(--feature-warm); }

  .card__rule {
    position: absolute;
    left: 0;
    right: 0;
    top: 334px;
    height: 3px;
  }
  .card--soft .card__rule  { background: var(--orange-line); }
  .card--vivid .card__rule { background: var(--white); }
  .card--airy .card__rule  { background: var(--orange-line); }
  .card--warm .card__rule  { background: var(--brand-red); }

  .brand {
    position: absolute;
    left: 13px;
    top: 316px;
    display: flex;
    align-items: flex-start;
    gap: 5px;
  }
  .brand__mark {
    width: 33px;
    height: 33px;
    border-radius: 50%;
    background: var(--orange);
    border: 2px solid var(--white);
    box-shadow: 0 0 0 1px var(--brand-red);
    margin-top: 2px;
  }
  .brand__name {
    font-size: 14px;
    font-weight: 600;
    line-height: 1;
    color: var(--brand-red);
    margin-top: 1px;
  }
  .card--warm .brand__name { color: var(--white); }

  .tagline {
    position: absolute;
    right: 12px;
    top: 340px;
    margin: 0;
    font-size: 7.5px;
    font-weight: 500;
    line-height: 1;
    letter-spacing: 1.6px;
    color: var(--ink-grey);
    text-transform: uppercase;
  }
</style>
</head>
<body>
<main class="canvas">

  <section class="card card--top-left card--soft">
    <div class="card__glow"></div>
    <div class="feature" aria-hidden="true"><span class="feature__ring"></span><p class="feature__name">Sun<br>Meadow</p></div>
    <div class="card__rule"></div>
    <div class="brand"><span class="brand__mark"></span><span class="brand__name">Sun Meadow</span></div>
    <p class="tagline">Coaching Services</p>
  </section>

  <section class="card card--top-right card--vivid">
    <div class="card__glow"></div>
    <div class="feature" aria-hidden="true"><span class="feature__ring"></span><p class="feature__name">Sun<br>Meadow</p></div>
    <div class="card__rule"></div>
    <div class="brand"><span class="brand__mark"></span><span class="brand__name">Sun Meadow</span></div>
    <p class="tagline">Coaching Services</p>
  </section>

  <section class="card card--bottom-left card--airy">
    <div class="card__glow"></div>
    <div class="feature" aria-hidden="true"><span class="feature__ring"></span><p class="feature__name">Sun<br>Meadow</p></div>
    <div class="card__rule"></div>
    <div class="brand"><span class="brand__mark"></span><span class="brand__name">Sun Meadow</span></div>
    <p class="tagline">Coaching Services</p>
  </section>

  <section class="card card--bottom-right card--warm">
    <div class="card__glow"></div>
    <div class="feature" aria-hidden="true"><span class="feature__ring"></span><p class="feature__name">Sun<br>Meadow</p></div>
    <div class="card__rule"></div>
    <div class="brand"><span class="brand__mark"></span><span class="brand__name">Sun Meadow</span></div>
    <p class="tagline">Coaching Services</p>
  </section>

</main>
</body>
</html>
```